K.E.T.A. The Halbrook Grand Jury Testimony

This is the cover artwork for the audio version
of the re-creation of the Halbrook Grand Jury testimony based around the killing of Darnell Wexby. I need a cover for the library binders. I have the template for the binder that I can send. The title of the audio is: K.E.T.A. I would like the words Halbrook Grand Jury Testimony added in somehow with some creative graphics. I have a website with other audio covers. I also need the words: Unabridged CD format somewhere at the bottom. Can I send the binder template later?

Target Market(s)

Audiobook

Industry/Entity Type

Audio

Font styles to use
Serif

Requirements
Nice to have
• no bullets, no blood, no dead bodies, no police, no police cars, no protest, no
• violent images, no bullets
Should not have
• nice clear sleek look

```html
<!DOCTYPE html>
<html lang="en">
<head>
<meta charset="utf-8">
<title>K.E.T.A. — Halbrook Grand Jury Testimony</title>
<link rel="stylesheet" href="https://fonts.googleapis.com/css2?family=Gentium+Book+Plus:wght@700&family=Libre+Franklin:wght@700;800&family=Source+Sans+3:wght@400&display=swap">
<style>
  :root {
    --night: #140604;
    --ember: #c83a0a;
    --flame: #ff7a12;
    --glow: #ffd24a;
    --cream: #fde7a2;
    --subtitle: #ff6312;
    --footnote: #6e5a50;
  }
  html, body {
    margin: 0;
    padding: 0;
    overflow: hidden;
    background: var(--night);
  }
  .cover {
    position: relative;
    width: 1200px;
    height: 1200px;
    overflow: hidden;
    background: var(--night);
  }
  .cover__scene {
    position: absolute;
    inset: 0;
    width: 1200px;
    height: 1200px;
  }
  .cover__title {
    position: absolute;
    top: 62px;
    left: 0;
    width: 1200px;
    margin: 0;
    text-align: center;
    font-family: "Gentium Book Plus", Georgia, serif;
    font-weight: 700;
    font-size: 262px;
    line-height: 1;
    letter-spacing: 4px;
    background: linear-gradient(100deg, var(--ember) 0%, var(--flame) 35%, var(--glow) 65%, var(--flame) 100%);
    -webkit-background-clip: text;
    background-clip: text;
    color: transparent;
    filter: drop-shadow(2px 3px 2px rgba(0,0,0,0.45));
  }
  .cover__case {
    position: absolute;
    top: 872px;
    left: 358px;
    width: 520px;
    text-align: center;
  }
  .cover__place {
    margin: 0;
    font-family: "Libre Franklin", Arial, sans-serif;
    font-weight: 800;
    font-size: 98px;
    line-height: 1;
    letter-spacing: -1px;
    color: var(--cream);
    text-transform: uppercase;
  }
  .cover__subtitle {
    margin: 4px 0 0;
    font-family: "Libre Franklin", Arial, sans-serif;
    font-weight: 700;
    font-size: 44px;
    line-height: 1.1;
    color: var(--subtitle);
  }
  .cover__format {
    position: absolute;
    top: 1130px;
    left: 0;
    width: 1200px;
    margin: 0;
    text-align: center;
    font-family: "Source Sans 3", Arial, sans-serif;
    font-size: 22px;
    color: var(--footnote);
  }
</style>
</head>
<body>
  <main class="cover">
    <svg class="cover__scene" viewBox="0 0 1200 1200" role="img" aria-label="Night crowd photograph bathed in orange firelight, a person holding up a hand-drawn portrait sign reading Justice for Darnell Wexby">
      <defs>
        <radialGradient id="scene-glow" cx="0.55" cy="0.5" r="0.6">
          <stop offset="0" stop-color="#fff3c0"/>
          <stop offset="0.12" stop-color="#ffc83a"/>
          <stop offset="0.38" stop-color="#f06a10"/>
          <stop offset="0.7" stop-color="#6a1a06"/>
          <stop offset="1" stop-color="#140604"/>
        </radialGradient>
        <linearGradient id="sign-tone" x1="0" y1="0" x2="0.6" y2="1">
          <stop offset="0" stop-color="#ff6a14"/>
          <stop offset="0.5" stop-color="#ffc22a"/>
          <stop offset="1" stop-color="#f07a12"/>
        </linearGradient>
      </defs>
      <rect width="1200" height="1200" fill="url(#scene-glow)"/>
      <polygon points="22,338 318,326 455,832 156,882" fill="url(#sign-tone)" opacity="0.85"/>
    </svg>

    <h1 class="cover__title">K.E.T.A.</h1>

    <div class="cover__case">
      <p class="cover__place">Halbrook</p>
      <p class="cover__subtitle">Grand Jury Testimony</p>
    </div>

    <p class="cover__format">Unabridged CD format</p>
  </main>
</body>
</html>
```